Business Card, Stationary Folder & Envelope
ORVALUX
Creative Brief
Bright & Fun-filled
Ramiro Quesada
TRL
Carretera Pueblanco - Ozumel Km 3.4, Colonia El Prado Tepalcingo, P.C. 90487, Tlaxcala, Tlax., México
VOXEL ID 57*83*40962
ramiro.quesada@orvalux.example
www.orvalux.example

```html
<!DOCTYPE html>
<html lang="es">
<head>
<meta charset="utf-8">
<title>ORVALUX – Tarjeta de presentación</title>
<link rel="stylesheet" href="https://fonts.googleapis.com/css2?family=Open+Sans:wght@400;600;800&display=swap">
<style>
  :root{
    --bg:#e9e7e3;
    --card:#ffffff;
    --band-dark:#0b0c0e;
    --band-blue:#1a86c4;
    --band-blue-deep:#0a4d7a;
    --brand-grey:#8c9094;
    --text:#3a3d40;
    --muted:#8e9297;
    --accent:#1f7fc0;
  }
  *{box-sizing:border-box;margin:0;padding:0}
  html,body{width:1200px;height:852px;overflow:hidden}
  body{background:var(--bg);font-family:"Open Sans",Arial,sans-serif;position:relative}
  .card{
    position:absolute;left:100px;top:140px;width:1000px;height:572px;
    background:var(--card);border-radius:34px;overflow:hidden;
    box-shadow:0 10px 30px rgba(0,0,0,.18);
  }
  .card__band{
    position:absolute;left:40px;top:0;width:170px;height:100%;
    background:linear-gradient(180deg,var(--band-dark) 0%,var(--band-dark) 34%,var(--band-blue-deep) 44%,var(--band-blue) 60%,var(--band-blue-deep) 78%,var(--band-dark) 92%);
  }
  .card__band::after{
    content:"";position:absolute;left:0;top:0;width:45%;height:100%;
    background:linear-gradient(90deg,rgba(255,255,255,.12),rgba(255,255,255,0));
  }
  .brand{position:absolute;left:40px;top:62px;display:flex;align-items:center;gap:22px}
  .brand__mark{width:110px;height:110px;border-radius:50%;background:var(--band-blue);margin-left:30px}
  .brand__name{font-weight:800;font-size:100px;letter-spacing:2px;color:var(--brand-grey);line-height:1}
  .address{position:absolute;left:240px;top:222px;font-size:22px;line-height:30px;color:var(--text)}
  .person{position:absolute;right:60px;top:330px;text-align:right}
  .person__name{font-size:32px;font-weight:600;color:var(--accent);line-height:1.2}
  .person__role{font-size:20px;color:var(--muted);margin-top:2px}
  .contacts{position:absolute;left:240px;top:340px;list-style:none}
  .contacts li{display:flex;align-items:center;gap:14px;font-size:22px;line-height:34px;color:var(--text)}
  .contacts svg{width:22px;height:22px;fill:var(--accent);flex:none}
</style>
</head>
<body>
  <article class="card">
    <div class="card__band"></div>
    <div class="brand">
      <span class="brand__mark"></span>
      <span class="brand__name">ORVALUX</span>
    </div>
    <p class="address">Carretera Pueblanco - Ozumel Km 3.4,<br>Colonia El Prado Tepalcingo,<br>P.C. 90487, Tlaxcala, Tlax., México</p>
    <div class="person">
      <p class="person__name">Ramiro Quesada</p>
      <p class="person__role">TRL</p>
    </div>
    <ul class="contacts">
      <li><svg viewBox="0 0 24 24"><path d="M7 2h10a2 2 0 0 1 2 2v16a2 2 0 0 1-2 2H7a2 2 0 0 1-2-2V4a2 2 0 0 1 2-2zm0 3v12h10V5zm5 13.5a1.2 1.2 0 1 0 0 2.4 1.2 1.2 0 0 0 0-2.4z"/></svg>VOXEL ID 57*83*40962</li>
      <li><svg viewBox="0 0 24 24"><path d="M6.6 10.8a15 15 0 0 0 6.6 6.6l2.2-2.2a1 1 0 0 1 1-.25 11.4 11.4 0 0 0 3.6.57 1 1 0 0 1 1 1V20a1 1 0 0 1-1 1A17 17 0 0 1 3 4a1 1 0 0 1 1-1h3.5a1 1 0 0 1 1 1c0 1.25.2 2.45.57 3.57a1 1 0 0 1-.25 1z"/></svg>+52 (246) 318-4072</li>
      <li><svg viewBox="0 0 24 24"><path d="M6.6 10.8a15 15 0 0 0 6.6 6.6l2.2-2.2a1 1 0 0 1 1-.25 11.4 11.4 0 0 0 3.6.57 1 1 0 0 1 1 1V20a1 1 0 0 1-1 1A17 17 0 0 1 3 4a1 1 0 0 1 1-1h3.5a1 1 0 0 1 1 1c0 1.25.2 2.45.57 3.57a1 1 0 0 1-.25 1z"/></svg>+52 (222) 741 26 58</li>
      <li><svg viewBox="0 0 24 24"><path d="M6 3h9v5H6zM4 9h16a2 2 0 0 1 2 2v6h-4v4H6v-4H2v-6a2 2 0 0 1 2-2zm4 7v3h8v-3z"/></svg>+52 (246) 318-5590</li>
      <li><svg viewBox="0 0 24 24"><path d="M3 5h18a1 1 0 0 1 1 1v12a1 1 0 0 1-1 1H3a1 1 0 0 1-1-1V6a1 1 0 0 1 1-1zm1 2.2V17h16V7.2l-8 5.3z"/></svg>ramiro.quesada@orvalux.example</li>
      <li><svg viewBox="0 0 24 24"><path d="M12 2a10 10 0 1 0 0 20 10 10 0 0 0 0-20zm6.9 9h-3a15 15 0 0 0-1.3-5.6A8 8 0 0 1 18.9 11zM12 4.1c.9 1.2 1.8 3.6 1.9 6.9h-3.8c.1-3.3 1-5.7 1.9-6.9zM9.4 5.4A15 15 0 0 0 8.1 11h-3a8 8 0 0 1 4.3-5.6zM5.1 13h3a15 15 0 0 0 1.3 5.6A8 8 0 0 1 5.1 13zm6.9 6.9c-.9-1.2-1.8-3.6-1.9-6.9h3.8c-.1 3.3-1 5.7-1.9 6.9zm2.6-1.3a15 15 0 0 0 1.3-5.6h3a8 8 0 0 1-4.3 5.6z"/></svg>www.orvalux.example</li>
    </ul>
  </article>
</body>
</html>
```